Business Card Design

we are a brand new cable TV network devoted to self improvement and leading a better life called FLOURIVO TV.I have a logo. We have 3 executives that need cards.I want it to be a heavy stock card: professional but showing our creative nature

Industry/Entity Type

Business

Contact Information for Business Card

CLAUDIA SAENZ AMLIECEO350 San Juan DrPonte Vedra Beach FL 32082904-473-5953

```html
<!DOCTYPE html>
<html lang="en">
<head>
<meta charset="utf-8">
<title>FLOURIVO TV – Business Card</title>
<link href="https://fonts.googleapis.com/css2?family=Questrial&display=swap" rel="stylesheet">
<style>
  :root {
    --backdrop: #e6e7ea;
    --card-white: #ffffff;
    --ink: #262426;
    --band-black: #242224;
    --accent-red: #c8202f;
    --text-light: #f4f4f4;
    --pattern-deep: #b3183f;
    --pattern-mid: #d8345a;
    --pattern-light: #e8648a;
  }
  * { margin: 0; padding: 0; box-sizing: border-box; }
  html, body {
    width: 1200px;
    height: 760px;
    overflow: hidden;
    background: var(--backdrop);
    font-family: "Questrial", "Century Gothic", sans-serif;
  }
  .card {
    position: absolute;
    left: 100px;
    top: 94px;
    width: 1000px;
    height: 572px;
    background: var(--card-white);
    box-shadow: 0 10px 30px rgba(0,0,0,0.18);
    overflow: hidden;
  }
  .brand {
    position: absolute;
    left: 0;
    top: 0;
    width: 100%;
    height: 296px;
    display: flex;
    align-items: center;
    justify-content: center;
    gap: 28px;
  }
  .brand-mark {
    width: 92px;
    height: 92px;
    background: var(--accent-red);
    border-radius: 14px;
  }
  .brand-name {
    font-size: 118px;
    letter-spacing: 2px;
    color: var(--ink);
    line-height: 1;
  }
  .info-band {
    position: absolute;
    left: 0;
    top: 296px;
    width: 100%;
    height: 160px;
    background: var(--band-black);
  }
  .person {
    position: absolute;
    right: 560px;
    top: 22px;
    text-align: right;
  }
  .person-name {
    font-size: 30px;
    letter-spacing: 1.5px;
    color: var(--text-light);
  }
  .person-title {
    margin-top: 6px;
    font-size: 24px;
    color: var(--accent-red);
    letter-spacing: 1px;
  }
  .divider {
    position: absolute;
    left: 470px;
    top: 18px;
    width: 3px;
    height: 124px;
    background: var(--text-light);
  }
  .contact {
    position: absolute;
    left: 505px;
    top: 18px;
    color: var(--text-light);
    font-size: 25px;
    letter-spacing: 1px;
    line-height: 1.4;
  }
  .contact-row {
    display: flex;
    align-items: flex-start;
    gap: 12px;
  }
  .contact-row + .contact-row { margin-top: 10px; }
  .contact-icon {
    width: 28px;
    height: 28px;
    flex: none;
    margin-top: 4px;
  }
  .pattern-band {
    position: absolute;
    left: 0;
    top: 456px;
    width: 100%;
    height: 116px;
    background: linear-gradient(100deg, var(--pattern-deep) 0%, var(--pattern-mid) 45%, var(--pattern-light) 75%, var(--pattern-mid) 100%);
  }
</style>
</head>
<body>
  <div class="card">
    <header class="brand">
      <span class="brand-mark"></span>
      <span class="brand-name">FLOURIVO TV</span>
    </header>

    <section class="info-band">
      <div class="person">
        <div class="person-name">Mirella Okafor Dunst</div>
        <div class="person-title">CEO</div>
      </div>

      <div class="divider"></div>

      <div class="contact">
        <div class="contact-row">
          <svg class="contact-icon" viewBox="0 0 24 24" aria-hidden="true">
            <path d="M3 11 L12 3 L21 11 M6 9 V21 H10 V15 H14 V21 H18 V9" fill="none" stroke="#c8202f" stroke-width="2.2" stroke-linejoin="round" stroke-linecap="round"/>
          </svg>
          <div>718 Harlow Creek Dr<br>Wrenhaven Shores NV 89410</div>
        </div>
        <div class="contact-row">
          <svg class="contact-icon" viewBox="0 0 24 24" aria-hidden="true">
            <path d="M6.6 10.8a15.1 15.1 0 0 0 6.6 6.6l2.2-2.2a1 1 0 0 1 1-.25 11.4 11.4 0 0 0 3.6.57 1 1 0 0 1 1 1V20a1 1 0 0 1-1 1A17 17 0 0 1 3 4a1 1 0 0 1 1-1h3.5a1 1 0 0 1 1 1 11.4 11.4 0 0 0 .57 3.6 1 1 0 0 1-.25 1z" fill="#c8202f"/>
          </svg>
          <div>555-618-2047</div>
        </div>
      </div>
    </section>

    <div class="pattern-band" role="img" aria-label="Decorative band of faceted pink and crimson triangles"></div>
  </div>
</body>
</html>
```